Business Card - connecting 2 souls and beggining the journey of self discovery

Logo on the front
with tag line

On the back list of services and contact details

Seminars
workshops
Coaching
podcasts

Daniel Porthwick
Health & Wellbeing Life Coach
0491 372 815
daniel@wovenpathwellness.example
wovenpathwellness.example

Industry/Entity Type

Life Coaching

Contact Information for Business Card

I like the use of colour from the logo to be used. I'm not a fan of white.

Requirements
Must have
• My tagline: The journey home starts with you
Nice to have
• Use of colour that is in the mind body soul logo

```html
<!DOCTYPE html>
<html lang="en">
<head>
<meta charset="utf-8">
<title>Woven Path Wellness – Business Card</title>
<link href="https://fonts.googleapis.com/css2?family=Questrial&family=Open+Sans:wght@400&display=swap" rel="stylesheet">
<style>
  :root {
    --backdrop: #939598;
    --card-white: #ffffff;
    --card-dark: #252325;
    --logo-panel: #1f1d1f;
    --brand-grey: #8a8d92;
    --leaf-green: #5f9430;
    --lime: #8cc63f;
    --soft-grey: #d6d6d6;
    --purple: #7b4f9e;
    --pink: #ee5f72;
    --teal: #45b2a8;
    --yellow: #f2bc1f;
  }
  * { box-sizing: border-box; margin: 0; padding: 0; }
  html, body { width: 1200px; height: 1200px; overflow: hidden; }
  body {
    background: var(--backdrop);
    font-family: "Questrial", "Century Gothic", sans-serif;
    position: relative;
  }
  .card {
    position: absolute;
    left: 220px;
    width: 760px;
    height: 460px;
    border-radius: 30px;
    overflow: hidden;
  }
  .card-front { top: 80px; background: var(--card-white); }
  .card-back { top: 620px; background: var(--card-dark); }

  .brand {
    display: flex;
    align-items: center;
    gap: 14px;
    color: var(--brand-grey);
    letter-spacing: -0.5px;
    white-space: nowrap;
  }
  .brand-dot { border-radius: 50%; background: var(--teal); flex: none; }

  .card-front .brand {
    position: absolute;
    top: 150px;
    left: 0; right: 0;
    justify-content: center;
    font-size: 34px;
  }
  .card-front .brand-dot { width: 38px; height: 38px; }
  .tagline {
    position: absolute;
    top: 300px;
    left: 0; right: 0;
    text-align: center;
    color: var(--leaf-green);
    font-size: 31px;
    letter-spacing: 0.3px;
  }

  .logo-panel {
    position: absolute;
    left: 60px; top: 95px;
    width: 220px; height: 150px;
    background: var(--logo-panel);
    display: flex; align-items: center; justify-content: center;
  }
  .logo-panel .brand { font-size: 19px; gap: 9px; }
  .logo-panel .brand-dot { width: 22px; height: 22px; }
  .divider {
    position: absolute;
    left: 318px; top: 80px;
    width: 3px; height: 140px;
    background: var(--soft-grey);
  }
  .contact {
    position: absolute;
    left: 360px; top: 70px;
  }
  .contact-name { color: var(--lime); font-size: 38px; line-height: 1.1; }
  .contact-role { color: var(--soft-grey); font-size: 20px; margin-top: 4px; letter-spacing: -0.3px; }
  .contact-list { list-style: none; margin-top: 22px; font-family: "Open Sans", Arial, sans-serif; color: #ffffff; font-size: 20px; }
  .contact-list li { display: flex; align-items: center; gap: 12px; line-height: 1.55; }
  .contact-list svg { width: 16px; height: 16px; fill: var(--lime); flex: none; }

  .services {
    position: absolute;
    left: 0; right: 0; bottom: 0;
    height: 72px;
    display: flex;
    list-style: none;
  }
  .services li {
    flex: 1;
    display: flex; align-items: center; justify-content: center;
    color: #ffffff; font-size: 26px; letter-spacing: 0.3px;
  }
  .service-seminars { background: var(--purple); }
  .service-workshops { background: var(--pink); }
  .service-coaching { background: var(--teal); }
  .service-podcasts { background: var(--yellow); }
</style>
</head>
<body>
  <section class="card card-front">
    <div class="brand"><span class="brand-dot"></span>Woven Path Wellness</div>
    <p class="tagline">The journey home starts with you</p>
  </section>

  <section class="card card-back">
    <div class="logo-panel">
      <div class="brand"><span class="brand-dot"></span>Woven Path Wellness</div>
    </div>
    <div class="divider"></div>
    <div class="contact">
      <h1 class="contact-name">Daniel Porthwick</h1>
      <p class="contact-role">Health &amp; Wellbeing Life Coach</p>
      <ul class="contact-list">
        <li>
          <svg viewBox="0 0 16 16" aria-hidden="true"><path d="M3.5 1 6 3.8 4.7 5.6c.9 2 2.6 3.8 4.7 4.7L11.2 9 14 11.5 12.3 14C7 13.6 2.4 9 2 3.7z"/></svg>
          0491 372 815
        </li>
        <li>
          <svg viewBox="0 0 16 16" aria-hidden="true"><path d="M1 3h14v10H1zM2.5 4.5 8 9l5.5-4.5z" fill-rule="evenodd"/></svg>
          daniel@wovenpathwellness.example
        </li>
        <li>
          <svg viewBox="0 0 16 16" aria-hidden="true"><path d="M8 1a7 7 0 1 0 0 14A7 7 0 0 0 8 1zm-.7 1.6v2.6H5.2c.4-1.4 1.2-2.4 2.1-2.6zm1.4 0c.9.2 1.7 1.2 2.1 2.6H8.7zM4 6.5h3.3v2.8H4a6 6 0 0 1 0-2.8zm4.7 0H12a6 6 0 0 1 0 2.8H8.7zm-3.5 4.2h2.1v2.7c-.9-.2-1.7-1.2-2.1-2.7zm3.5 0h2.1c-.4 1.5-1.2 2.5-2.1 2.7z"/></svg>
          wovenpathwellness.example
        </li>
      </ul>
    </div>
    <ul class="services">
      <li class="service-seminars">Seminars</li>
      <li class="service-workshops">Workshops</li>
      <li class="service-coaching">Coaching</li>
      <li class="service-podcasts">Podcasts</li>
    </ul>
  </section>
</body>
</html>
```